Website Design For our Tour Company

We need a face lift on our current website. I want it to look the best! Lots of videos. An easy to use website to obtain easy conversions. I want people to feel like they are on the tour just by looking at our website. My current website is just bland and unprofessional looking. I want it to be incredibly mobile friendly and look great on the desk top. Our current website is https://www.kellbrookvoyages.example/
I would like there to be an option where the viewer can select what language they would like to read in. Im hoping you can pull a-lot of media and videos from out facebook page. Im not happy with most of my descriptions for the product and tours we offer. Looking for professional help.

Our two main activities are Summer and Winter Tours
In The Summer the main things we do our Jet Boat & Jet Ski Tours.

In The Winter our main tour is luxury first class Aurora Viewing. I Would like to see a-lot of aurora video/photos as I believe that gets peoples attention!

Target Market(s)

Travelers from china and around the world

Coding

Coded - Design and coding required

Number of Pages Required

5+ page

Requirements
Must have
• be able to select what when language you would like to read the website in.
Nice to have
• The overall look and feel I want for the website is luxury, fancy, royalty. Think Gerald Mossworth. I like the Luxury gold colors. I need the website to look ridiculously professional

incorporate Lots of Aurora photos / videos as one of our main tours is Aurora

```html
<!DOCTYPE html>
<html lang="en">
<head>
<meta charset="utf-8">
<title>Kellbrook Voyages — Guided Tours</title>
<link rel="stylesheet" href="https://fonts.googleapis.com/css2?family=Michroma&family=Open+Sans:wght@400;600&display=swap">
<style>
:root{
  --ink:#000;
  --gold:#efe2a8;
  --cream:#f3e7b4;
  --white:#fff;
  --head:"Michroma", sans-serif;
  --body:"Open Sans", sans-serif;
}
*{box-sizing:border-box;margin:0;padding:0}
html,body{width:1200px;height:4831px;overflow:hidden;background:var(--ink);font-family:var(--body);color:var(--white)}
.page{position:relative;width:1200px;height:4831px}
.abs{position:absolute}
.photo{position:absolute;display:block}
.h-title{font-family:var(--head);color:var(--gold);text-align:center;text-transform:uppercase;letter-spacing:1px;white-space:nowrap}
.btn-outline{position:absolute;border:3px solid var(--gold);color:var(--gold);font-family:var(--head);font-size:12px;display:flex;align-items:center;justify-content:center;text-transform:uppercase;white-space:nowrap;border-radius:3px}

/* top bar + header */
.topbar{top:0;left:0;width:1200px;height:30px;background:var(--ink);font-size:13px;font-weight:600}
.topbar .phone{left:66px;top:7px}
.topbar .social{right:190px;top:8px;display:flex;gap:10px}
.dot{width:13px;height:13px;border-radius:50%;background:var(--white)}
.topbar .switchers{right:66px;top:7px;display:flex;gap:14px;font-size:12px}
.header{top:30px;left:0;width:1200px;height:109px;background:var(--ink);border-bottom:1px solid #222}
.brand{left:86px;top:14px;width:110px;text-align:center;color:var(--gold);font-family:var(--head)}
.brand .mark{width:46px;height:46px;border-radius:50%;background:var(--gold);margin:0 auto 6px}
.brand .name{font-size:11px;letter-spacing:1px}
.nav{left:368px;top:44px;display:flex;gap:42px;font-size:15px;font-weight:600}
.nav .active{color:var(--gold)}
.book-online{right:86px;top:33px;width:130px;height:44px;background:var(--gold);color:#111;font-size:14px;font-weight:600;border-radius:3px;display:flex;align-items:center;justify-content:center}

/* hero */
.hero{top:139px;left:0;width:1200px;height:615px;background:linear-gradient(180deg,#2d3e58 0%,#c9834b 22%,#6a5640 40%,#4a3a2c 65%,#2b2219 100%)}
.hero h1{position:absolute;left:66px;top:142px;font-family:var(--head);color:var(--gold);font-size:46px;line-height:74px;letter-spacing:3px;font-weight:400;white-space:nowrap}
.tour-btn{position:absolute;top:318px;height:42px;font-size:15px;display:flex;align-items:center;justify-content:center;white-space:nowrap}
.tour-btn.summer{left:66px;width:150px;background:var(--gold);color:#111}
.tour-btn.winter{left:256px;width:148px;border:2px solid var(--white);color:var(--white)}
.field{position:absolute;top:528px;height:42px;background:var(--white);color:#666;font-size:13px;display:flex;align-items:center;justify-content:space-between;padding:0 14px}
.book-now{position:absolute;top:528px;left:850px;width:230px;height:42px;background:var(--gold);color:#111;font-family:var(--head);font-size:15px;display:flex;align-items:center;justify-content:center}

/* about */
.about{top:754px;left:0;width:1200px;height:770px}
.about .h-title{position:absolute;left:0;width:1200px}
.about p{position:absolute;left:0;width:1200px;text-align:center;font-size:13px;line-height:23px}
.arrow{position:absolute}
.video-play{position:absolute;left:124px;top:100px;width:78px;height:40px;border:3px solid rgba(255,255,255,.85);border-radius:10px}

/* trip band */
.trip{top:1524px;left:0;width:1200px;height:580px;background:linear-gradient(180deg,#4a5a68 0%,#2c4046 35%,#1d2a26 65%,#0f1514 100%)}
.trip .h-title{position:absolute;left:0;width:1200px;font-size:33px;line-height:54px}
.trip p{position:absolute;left:258px;width:684px;text-align:center;font-size:13px;line-height:23px}

/* gallery */
.gallery-grid{position:absolute;top:2282px;left:0;display:grid;grid-template-columns:repeat(4,300px);grid-template-rows:repeat(2,262.5px)}
.eye-frame{position:absolute;left:22px;top:22px;width:256px;height:218px;border:5px solid rgba(255,255,255,.85)}

/* contact */
.contact-panel{top:2981px;left:624px;width:576px;height:510px;background:var(--cream);color:#111}
.contact-panel h2{position:absolute;left:46px;top:40px;font-family:var(--head);font-size:34px;font-weight:400;white-space:nowrap}
.line-field{position:absolute;left:46px;width:430px;border-bottom:2px solid #333;font-family:var(--head);font-size:11px;padding-bottom:8px}
.submit{position:absolute;left:196px;top:423px;width:132px;height:44px;border:3px solid #111;font-family:var(--head);font-size:12px;display:flex;align-items:center;justify-content:center;border-radius:3px}

/* blog */
.blog-card{position:absolute;top:3652px;width:319px;height:246px;border-radius:4px;overflow:hidden}
.blog-card span{position:absolute;left:18px;bottom:22px;font-family:var(--head);font-size:13px;line-height:22px;color:var(--gold);white-space:nowrap}

/* newsletter */
.newsletter{top:4069px;left:0;width:1200px;height:450px;background:linear-gradient(160deg,#6b6e6e 0%,#8a7f76 35%,#5a4a3a 60%,#c68a28 100%)}
.newsletter .kicker{position:absolute;left:0;width:1200px;top:140px;text-align:center;font-family:var(--head);font-size:15px;color:var(--gold)}
.newsletter h2{position:absolute;left:0;width:1200px;top:172px;text-align:center;font-family:var(--head);font-size:36px;color:var(--gold);font-weight:400;white-space:nowrap}
.nl-email{position:absolute;left:332px;top:270px;width:406px;height:54px;background:var(--white);color:#111;font-family:var(--head);font-size:12px;display:flex;align-items:center;padding-left:14px}
.nl-btn{position:absolute;left:738px;top:270px;width:130px;height:54px;background:var(--gold);color:#111;font-family:var(--head);font-size:15px;display:flex;align-items:center;justify-content:center;white-space:nowrap}

/* footer */
.footer{top:4519px;left:0;width:1200px;height:312px;background:var(--ink)}
.footer .mark{position:absolute;left:556px;top:40px;width:88px;height:88px;border-radius:50%;background:var(--gold)}
.footer .fname{position:absolute;left:0;width:1200px;top:140px;text-align:center;font-family:var(--head);color:var(--gold);font-size:11px;letter-spacing:1px}
.fnav{position:absolute;left:0;width:1200px;top:178px;display:flex;justify-content:center;gap:40px;font-family:var(--head);font-size:13px}
.fsocial{position:absolute;left:0;width:1200px;top:220px;display:flex;justify-content:center;gap:14px}
.fsocial .dot{width:20px;height:20px}
.frule{position:absolute;left:86px;width:1028px;top:258px;border-top:1px solid #444}
.copy{position:absolute;left:0;width:1200px;top:280px;text-align:center;font-family:var(--head);font-size:12px;letter-spacing:1px}
</style>
</head>
<body>
<div class="page">

  <div class="abs topbar">
    <div class="abs phone">PHONE&nbsp; 555-014-2780</div>
    <div class="abs social"><span class="dot"></span><span class="dot"></span><span class="dot"></span><span class="dot"></span></div>
    <div class="abs switchers"><span class="language" aria-label="Select language">EN ▾</span><span class="currency">INR ▾</span></div>
  </div>

  <header class="abs header">
    <div class="abs brand"><div class="mark"></div><div class="name">KELLBROOK</div></div>
    <nav class="abs nav"><span class="active">HOME</span><span>ABOUT US</span><span>CAR RENTAL'S</span><span>BLOG</span><span>CONTACT</span></nav>
    <div class="abs book-online">BOOK ONLINE</div>
  </header>

  <section class="abs hero" role="img" aria-label="Photo of a stone wall winding over mountains at sunset">
    <h1>GREAT DEALS<br>ON GUIDED TOURS</h1>
    <div class="tour-btn summer">SUMMER TOURS</div>
    <div class="tour-btn winter">WINTER TOURS</div>
    <div class="field" style="left:120px;width:228px">NAME</div>
    <div class="field" style="left:363px;width:228px">DESTINATION <svg width="10" height="7"><path d="M1 1l4 4 4-4" stroke="#666" fill="none" stroke-width="1.5"/></svg></div>
    <div class="field" style="left:606px;width:228px">DATE <svg width="10" height="7"><path d="M1 1l4 4 4-4" stroke="#666" fill="none" stroke-width="1.5"/></svg></div>
    <div class="book-now">BOOK NOW</div>
  </section>

  <section class="abs about">
    <h2 class="h-title" style="top:82px;font-size:34px;font-weight:400">ABOUT US</h2>
    <div class="h-title" style="position:absolute;left:0;width:1200px;top:150px;font-size:15px">GREAT JOURNEYS. FASCINATING PLACES.</div>
    <p style="top:196px">Local Experts Theo, Lena, and Corbin</p>
    <p style="top:243px">Corbin - Life-long Alaskan - Local expert, loves the outdoors, construction, &amp; adventures<br>Theo - Life-long Alaskan - Local expert entrepreneur, loves Alaska, always ready for an adventure and a fun time!<br>Lena - Life-long Alaska - Local expert, company cook, organizes the activities &amp; schedule. Without her we have no organization.</p>
    <div class="btn-outline" style="left:534px;top:340px;width:132px;height:44px">READ MORE</div>
    <svg class="arrow" style="left:66px;top:538px" width="14" height="24"><path d="M12 2L3 12l9 10" stroke="#fff" stroke-width="3" fill="none"/></svg>
    <svg class="arrow" style="left:1118px;top:538px" width="14" height="24"><path d="M2 2l9 10-9 10" stroke="#fff" stroke-width="3" fill="none"/></svg>
    <div class="photo" style="left:96px;top:440px;width:326px;height:242px;border-radius:4px;background:linear-gradient(180deg,#a9c4dc 0%,#3e6a3a 35%,#2c4a5c 60%,#1c3242 100%)" role="img" aria-label="Photo of kayakers paddling on a river lined with trees"></div>
    <div class="photo" style="left:437px;top:440px;width:326px;height:242px;border-radius:4px;background:linear-gradient(180deg,#9fb4d8 0%,#6d84b8 50%,#4b5f93 100%)" role="img" aria-label="Video still of a person bathing in a misty hot spring">
      <div class="video-play"><svg width="72" height="34" style="position:absolute;left:0;top:0"><path d="M30 8l14 9-14 9z" fill="rgba(255,255,255,.9)"/></svg></div>
    </div>
    <div class="photo" style="left:778px;top:440px;width:326px;height:242px;border-radius:4px;background:linear-gradient(180deg,#c8d0d4 0%,#5a6a50 35%,#3a4a52 60%,#c8a030 100%)" role="img" aria-label="Photo of a rider on a jet ski on a river"></div>
  </section>

  <section class="abs trip" role="img" aria-label="Photo of a red kayak on a calm lake at dusk beneath dark spruce trees">
    <h2 class="h-title" style="top:142px;font-weight:400">TAKE YOUR NEXT TRIP WITH<br>KELLBROOK VOYAGES, LLC</h2>
    <div class="h-title" style="position:absolute;left:0;width:1200px;top:276px;font-size:16px">THE ONLY TRAVEL AGENCY FOR YOU</div>
    <p style="top:316px">Kellbrook Voyages, LLC specializes in providing the best travel services in Fairbanks, Alaska. We've been in Fairbanks since 1995, creating customized itineraries for our clients based around their personal plans and preferences. In our line of work we don't only make plans, we help you build experiences and memories. Let us arrange the details of your next trip — call today for a free consultation.</p>
  </section>

  <h2 class="abs h-title" style="left:0;width:1200px;top:2184px;font-size:34px;font-weight:400">OUR GALLERY</h2>
  <div class="gallery-grid">
    <div class="photo" style="position:relative;background:linear-gradient(160deg,#8a7a60,#4a4638 60%,#2a2a26)" role="img" aria-label="Photo of a rider on a jet ski"></div>
    <div class="photo" style="position:relative;background:#e9e4c8" role="img" aria-label="Photo of an eagle perched on a treetop">
      <div class="eye-frame"></div>
      <svg style="position:absolute;left:128px;top:118px" width="44" height="26"><path d="M2 13C10 2 34 2 42 13 34 24 10 24 2 13z" fill="#111"/><circle cx="22" cy="13" r="6" fill="#e9e4c8"/><circle cx="22" cy="13" r="3" fill="#111"/></svg>
    </div>
    <div class="photo" style="position:relative;background:linear-gradient(180deg,#a8aec4,#c8c8d4 50%,#e0dcd8)" role="img" aria-label="Photo of two people ice fishing in the snow"></div>
    <div class="photo" style="position:relative;background:linear-gradient(180deg,#c4ccd0,#5a6a48 35%,#6a7c8c 60%,#c8a830)" role="img" aria-label="Photo of two riders on a jet ski"></div>
    <div class="photo" style="position:relative;background:linear-gradient(180deg,#9aa8bc,#3a3a44 50%,#c8ccd8)" role="img" aria-label="Photo of a person holding a fish in winter"></div>
    <div class="photo" style="position:relative;background:linear-gradient(180deg,#2e74c8,#2a5a2c 40%,#1c3c48 70%,#2a4c5a)" role="img" aria-label="Photo of a jet ski parked on a lake shore"></div>
    <div class="photo" style="position:relative;background:linear-gradient(180deg,#5a5a7a,#c8a078 60%,#1a1a1a)" role="img" aria-label="Photo of a forest silhouette at sunset"></div>
    <div class="photo" style="position:relative;background:linear-gradient(160deg,#6a90c8,#3a6aa0 50%,#b03030)" role="img" aria-label="Photo of jet ski handlebars over a lake"></div>
  </div>
  <div class="btn-outline" style="left:534px;top:2850px;width:132px;height:44px">VIEW ALL</div>

  <div class="photo" style="top:2981px;left:0;width:624px;height:510px;background:linear-gradient(180deg,#7a9ac0 0%,#d8c088 45%,#f0b848 58%,#a8b8d0 72%,#e8eef4 100%)" role="img" aria-label="Photo of a mug beside a birch tree over a misty frozen river at sunrise"></div>
  <section class="abs contact-panel">
    <h2>CONTACT US</h2>
    <div class="line-field" style="top:124px">NAME</div>
    <div class="line-field" style="top:174px">EMAIL</div>
    <div class="line-field" style="top:224px">PHONE</div>
    <div class="line-field" style="top:272px">SUBJECT</div>
    <div class="line-field" style="top:324px;height:60px">MESSAGE</div>
    <div class="submit">SUBMIT</div>
  </section>

  <h2 class="abs h-title" style="left:0;width:1200px;top:3574px;font-size:34px;font-weight:400">BLOG POST</h2>
  <svg class="arrow" style="left:66px;top:3758px" width="14" height="24"><path d="M12 2L3 12l9 10" stroke="#fff" stroke-width="3" fill="none"/></svg>
  <svg class="arrow" style="left:1118px;top:3758px" width="14" height="24"><path d="M2 2l9 10-9 10" stroke="#fff" stroke-width="3" fill="none"/></svg>
  <div class="blog-card" style="left:103px;background:linear-gradient(180deg,#8aa0c4,#e0b878 40%,#6a6a70 70%,#3a3a3e)" role="img" aria-label="Photo of a misty river at sunrise"><span>DRIVE A RENTAL CAR OR<br>BOOK A GUIDED TRIP.....</span></div>
  <div class="blog-card" style="left:441px;background:linear-gradient(180deg,#5a4a7a,#3a2e5a 50%,#1a1a2a)" role="img" aria-label="Photo of a rider on a jet ski at dusk"><span>TOP 5 THINGS TO DO IN<br>FAIRBANKS ALASKA</span></div>
  <div class="blog-card" style="left:778px;background:linear-gradient(180deg,#c4ccd0,#4a5a44 35%,#5a6a7a 60%,#3a3a40)" role="img" aria-label="Photo of two riders on a jet ski"><span>THE PERFECT AURORA<br>PICTURE</span></div>
  <div class="btn-outline" style="left:534px;top:3939px;width:132px;height:44px">VIEW ALL</div>

  <section class="abs newsletter" role="img" aria-label="Photo of a smiling rider on a jet ski on a river">
    <div class="kicker">TO RECEIVE OUR BEST MONTHLY DEALS</div>
    <h2>JOIN THE NEWSLETTER</h2>
    <div class="nl-email">EMAIL</div>
    <div class="nl-btn">SING UP</div>
  </section>

  <footer class="abs footer">
    <div class="mark"></div>
    <div class="fname">KELLBROOK VOYAGES</div>
    <nav class="fnav"><span>HOME</span><span>ABOUT US</span><span>CAR RENTAL'S</span><span>BLOG</span><span>CONTACT</span></nav>
    <div class="fsocial"><span class="dot"></span><span class="dot"></span><span class="dot"></span><span class="dot"></span></div>
    <div class="frule"></div>
    <div class="copy">COPYRIGHT © 2020 KELLBROOK VOYAGES, LLC. ALL RIGHTS RESERVED.</div>
  </footer>

</div>
</body>
</html>
```